KPT Building And Maintenance

Need a very professional looking double sided Buisiness card with all my details phone number, name, email, license number.

Target Market(s)

construction industry

Industry/Entity Type

building

Contact Information for Business Card

Name Dale Whitcombe. Email Address Info@KPTBuilding.example.au mobile number 0452918730 licence number 871406D. web site

```html
<!DOCTYPE html>
<html lang="en">
<head>
<meta charset="utf-8">
<title>KPT Building And Maintenance – Business Card</title>
<link href="https://fonts.googleapis.com/css2?family=Montserrat:wght@700;800&family=Roboto:wght@400;500;700&display=swap" rel="stylesheet">
<style>
  :root {
    --backdrop: #e9e6e1;
    --panel-grey: #4a4b4e;
    --panel-black: #0b0b0c;
    --brand-blue: #3a8fd8;
    --line-blue: #2f86d2;
    --photo-deep: #2d4f72;
    --photo-mid: #5d8fbf;
    --photo-light: #b9d3ea;
    --paper: #f4f5f7;
    --ink: #1c1d1f;
    --ink-soft: #3a3b3e;
    --white: #ffffff;
  }
  * { box-sizing: border-box; margin: 0; padding: 0; }
  html, body { width: 900px; height: 1200px; overflow: hidden; }
  body { background: var(--backdrop); position: relative; font-family: "Roboto", Arial, sans-serif; }

  .card {
    position: absolute; left: 73px; width: 777px; height: 452px;
    border-radius: 22px; overflow: hidden;
    box-shadow: 0 6px 18px rgba(0,0,0,.18);
  }
  .card--front { top: 130px; }
  .card--back { top: 620px; height: 458px; }

  .photo { position: absolute; inset: 0; }
  .photo--grinding {
    background: linear-gradient(135deg, var(--photo-deep) 0%, var(--photo-mid) 45%, var(--photo-light) 75%, var(--photo-mid) 100%);
  }
  .photo--excavator {
    background: linear-gradient(160deg, var(--photo-light) 0%, #dbe7f2 30%, var(--photo-mid) 62%, #8fb0cf 85%, var(--photo-deep) 100%);
  }

  .shapes { position: absolute; inset: 0; width: 100%; height: 100%; }

  .holder-name {
    position: absolute; left: 54px; top: 62px;
    font-family: "Montserrat", Arial, sans-serif; font-weight: 800;
    line-height: 1.08; letter-spacing: 1px; text-transform: uppercase;
  }
  .holder-name__first { color: var(--white); font-size: 42px; display: block; }
  .holder-name__last { color: var(--brand-blue); font-size: 38px; display: block; }
  .licence {
    position: absolute; left: 54px; top: 168px;
    color: var(--white); font-size: 18px; letter-spacing: .3px;
  }

  .contact {
    position: absolute; left: 39px; width: 381px; height: 42px;
    background: var(--paper); border-radius: 21px;
    display: flex; align-items: center; gap: 14px; padding-left: 6px;
    color: var(--ink); font-weight: 700;
  }
  .contact--phone { top: 314px; font-size: 25px; letter-spacing: .5px; }
  .contact--email { top: 364px; font-size: 19px; }
  .contact__icon {
    width: 32px; height: 32px; border-radius: 50%;
    background: var(--ink-soft); display: flex; align-items: center; justify-content: center;
    flex: none;
  }

  .brand-name {
    position: absolute; text-align: center;
    font-family: "Montserrat", Arial, sans-serif; font-weight: 800;
    text-transform: uppercase; line-height: 1;
  }
  .brand-name--front { left: 575px; top: 318px; width: 160px; color: var(--ink-soft); }
  .brand-name--front .brand-name__main { font-size: 54px; display: block; }
  .brand-name--front .brand-name__sub { font-size: 22px; display: block; margin-top: 6px; letter-spacing: 1px; }
  .brand-name--back { left: 60px; top: 82px; width: 240px; color: var(--white); }
  .brand-name--back .brand-name__main { font-size: 84px; display: block; }
  .brand-name--back .brand-name__sub { font-size: 33px; display: block; margin-top: 8px; letter-spacing: 1.5px; }

  .website {
    position: absolute; left: 357px; top: 372px; width: 338px; height: 38px;
    background: var(--white); border-radius: 4px;
    display: flex; align-items: center; justify-content: center;
    color: var(--ink); font-weight: 700; font-size: 21px;
  }
</style>
</head>
<body>

<section class="card card--front" aria-label="Business card front">
  <div class="photo photo--grinding" role="img" aria-label="Blue-toned photo of a worker cutting metal with an angle grinder, sparks flying"></div>
  <svg class="shapes" viewBox="0 0 777 452" preserveAspectRatio="none" aria-hidden="true">
    <path d="M0,0 H548 L378,240 Q362,263 334,265 H0 Z" fill="var(--panel-grey)"/>
    <rect x="0" y="256" width="232" height="4" fill="var(--white)"/>
    <path d="M445,452 L565,292 Q582,268 612,265 H777 V452 Z" fill="var(--paper)"/>
    <line x1="444" y1="450" x2="550" y2="324" stroke="var(--line-blue)" stroke-width="4"/>
  </svg>

  <h1 class="holder-name">
    <span class="holder-name__first">Dale</span>
    <span class="holder-name__last">Whitcombe</span>
  </h1>
  <p class="licence">LICENCE NUMBER 871406D</p>

  <div class="contact contact--phone">
    <span class="contact__icon">
      <svg width="14" height="20" viewBox="0 0 14 20" aria-hidden="true">
        <rect x="1" y="1" width="12" height="18" rx="2" fill="none" stroke="#fff" stroke-width="1.8"/>
        <line x1="5" y1="16" x2="9" y2="16" stroke="#fff" stroke-width="1.6"/>
      </svg>
    </span>
    <span>045 291 8730</span>
  </div>
  <div class="contact contact--email">
    <span class="contact__icon">
      <svg width="18" height="13" viewBox="0 0 18 13" aria-hidden="true">
        <rect x="1" y="1" width="16" height="11" rx="1.5" fill="none" stroke="#fff" stroke-width="1.6"/>
        <path d="M1.5,1.5 L9,7.5 L16.5,1.5" fill="none" stroke="#fff" stroke-width="1.6"/>
      </svg>
    </span>
    <span>Info@KPTBuilding.example.au</span>
  </div>

  <div class="brand-name brand-name--front">
    <span class="brand-name__main">KPT</span>
    <span class="brand-name__sub">Building</span>
  </div>
</section>

<section class="card card--back" aria-label="Business card back">
  <div class="photo photo--excavator" role="img" aria-label="Blue-toned photo of a compact excavator working on a gravel building site"></div>
  <svg class="shapes" viewBox="0 0 777 458" preserveAspectRatio="none" aria-hidden="true">
    <path d="M0,0 H532 L340,250 Q322,272 292,272 H0 Z" fill="var(--panel-black)"/>
    <line x1="538" y1="2" x2="392" y2="172" stroke="var(--white)" stroke-width="4"/>
  </svg>

  <div class="brand-name brand-name--back">
    <span class="brand-name__main">KPT</span>
    <span class="brand-name__sub">Building</span>
  </div>

  <div class="website">www.KPTBuilding.example.au</div>
</section>

</body>
</html>
```